Banner for back of trucks

We make a product that is called "Brindo".
It attaches to the side of hay balers and automatically applies tags to bales as they are being made.
We require a simple / modern banner design that will be affixed to the back of hay trucks showing that the hay on board has been Marked by Brindo.
The banner will be 52x91cm (landscape)
The banner needs to say "Marked by Brindo" using the company logo.
It also needs the website "www.brindo.com.au" displayed.
We have attached an image of our logo, the product itself and the back of a truck it will be attached to for reference.

```html
<!DOCTYPE html>
<html lang="en">
<head>
<meta charset="utf-8">
<title>Marked by Brindo – Truck Banner</title>
<link rel="stylesheet" href="https://fonts.googleapis.com/css2?family=Montserrat:wght@500;800&display=swap">
<style>
  :root {
    --page-bg: #f3f3f3;
    --banner-orange: #fdad33;
    --banner-brown: #5a4739;
    --brand-white: #ffffff;
  }
  * { margin: 0; padding: 0; box-sizing: border-box; }
  html, body {
    width: 1200px;
    height: 1200px;
    overflow: hidden;
    background: var(--page-bg);
  }
  .banner {
    position: absolute;
    left: 55px;
    top: 288px;
    width: 1090px;
    height: 624px;
    background: var(--banner-orange);
    font-family: "Montserrat", sans-serif;
    color: var(--banner-brown);
  }
  .banner__tagline {
    position: absolute;
    left: 0;
    right: 0;
    top: 102px;
    text-align: center;
    font-weight: 500;
    font-size: 104px;
    line-height: 1;
    letter-spacing: 1px;
  }
  .banner__band {
    position: absolute;
    left: 0;
    right: 0;
    top: 235px;
    height: 195px;
    background: var(--banner-brown);
    display: flex;
    align-items: center;
    justify-content: center;
  }
  .brand-name {
    font-weight: 800;
    font-size: 160px;
    line-height: 1;
    letter-spacing: 4px;
    color: var(--brand-white);
    transform: translateY(-6px);
  }
  .banner__web {
    position: absolute;
    left: 0;
    right: 0;
    top: 500px;
    height: 80px;
    display: flex;
    align-items: center;
  }
  .web-rule {
    height: 7px;
    background: var(--banner-brown);
  }
  .web-rule--left { width: 213px; }
  .web-rule--right { flex: 1; }
  .web-address {
    padding: 0 24px;
    font-weight: 500;
    font-size: 54px;
    letter-spacing: 5px;
    line-height: 1;
    white-space: nowrap;
  }
</style>
</head>
<body>
  <div class="banner">
    <p class="banner__tagline">Marked by</p>
    <div class="banner__band">
      <span class="brand-name">Brindo</span>
    </div>
    <div class="banner__web">
      <span class="web-rule web-rule--left"></span>
      <span class="web-address">www.brindo.com.au</span>
      <span class="web-rule web-rule--right"></span>
    </div>
  </div>
</body>
</html>
```